Website Design - Financial Services Software

We are looking for website designs for our public website.
Some competitor sites we like are
www.torvani.com.au
www.pluma.com.au
www.quentabridge.com
www.morlupa.com.au

A wireframe example of our site can be found at
http://pr4tqz.bivlowpage.com/

Attached is our logo.

Industry/Entity Type

Financial

```html
<!DOCTYPE html>
<html lang="en">
<head>
<meta charset="utf-8">
<title>Veltrano – Business Solutions</title>
<link href="https://fonts.googleapis.com/css2?family=Arimo:wght@400&family=PT+Sans+Narrow:wght@400&family=Roboto:wght@400&display=swap" rel="stylesheet">
<style>
  :root {
    --backdrop: #520303;
    --page: #e6e6e6;
    --page-light: #efeeee;
    --panel: #ebeaea;
    --brand-red: #b40d0d;
    --ink: #111111;
    --tab-top: #4a4a4a;
    --tab-mid: #1a1a1a;
    --tab-bottom: #000000;
    --side-red: #a30808;
    --side-dark: #140000;
    --white: #ffffff;
  }
  * { margin: 0; padding: 0; box-sizing: border-box; }
  html, body { width: 1200px; height: 900px; overflow: hidden; }
  body { background: var(--backdrop); font-family: "Arimo", Arial, sans-serif; color: var(--ink); position: relative; }

  .page {
    position: absolute; left: 153px; top: 13px; width: 878px; height: 900px;
    background: linear-gradient(180deg, var(--page-light) 0%, var(--page) 100%);
  }

  .brand { position: absolute; left: 40px; top: 48px; width: 140px; height: 140px; }
  .brand-dot { position: absolute; left: 98px; top: 10px; width: 74px; height: 74px; border-radius: 50%; background: var(--brand-red); }
  .brand-name {
    position: absolute; left: 8px; top: 107px;
    font-family: "Roboto", Arial, sans-serif; font-size: 27px; color: var(--brand-red); letter-spacing: 0.2px;
  }

  .masthead { position: absolute; left: 219px; top: 72px; }
  .masthead-title { font-family: "Roboto", Arial, sans-serif; font-weight: 400; font-size: 57px; line-height: 60px; letter-spacing: -0.5px; color: var(--ink); }
  .masthead-title span { color: var(--brand-red); }
  .masthead-tagline { font-family: "Roboto", Arial, sans-serif; font-size: 24px; line-height: 28px; color: var(--brand-red); letter-spacing: -0.2px; }

  .top-nav { position: absolute; left: 219px; top: 217px; display: flex; }
  .top-nav a {
    display: block; width: 135.25px; height: 43px; text-decoration: none; color: var(--white);
    font-family: "PT Sans Narrow", Arial, sans-serif; font-size: 26px; line-height: 38px; text-align: center;
    background: linear-gradient(180deg, var(--tab-top) 0%, var(--tab-mid) 50%, var(--tab-bottom) 51%, #222 100%);
    border: 1px solid #000; border-right: 1px solid #555;
  }

  .content-panel {
    position: absolute; left: 62px; top: 266px; width: 792px; height: 700px; border-radius: 9px 9px 0 0;
    background: linear-gradient(90deg, #e0e0e0 0%, var(--panel) 12%, var(--panel) 100%);
  }

  .side-nav { position: absolute; left: 62px; top: 355px; width: 136px; border: 1px solid #000; }
  .side-nav a {
    display: block; height: 47px; padding-left: 8px; text-decoration: none; color: var(--white);
    font-family: "PT Sans Narrow", Arial, sans-serif; font-size: 18px; line-height: 36px;
    background: linear-gradient(180deg, var(--side-red) 0%, #5a0303 50%, var(--side-dark) 55%, #3a0505 100%);
    border-bottom: 1px solid #000;
  }
  .side-nav a:last-child { border-bottom: none; }

  .main { position: absolute; left: 219px; top: 326px; width: 636px; }
  .main h1 { font-family: "Arimo", Arial, sans-serif; font-weight: 400; font-size: 24px; line-height: 28px; letter-spacing: -0.4px; margin-bottom: 18px; }
  .main p { font-size: 14px; line-height: 18.3px; letter-spacing: -0.35px; margin-bottom: 18px; }
  .chart-row { display: flex; gap: 21px; margin: 0 0 24px; }
  .chart { width: 178px; height: 150px; }
  .chart-warm { background: linear-gradient(160deg, #ffffff 20%, #d9622a 60%, #ffe7a8 100%); }
  .chart-green { background: linear-gradient(160deg, #ffffff 20%, #7db326 60%, #e8efcf 100%); }
  .chart-blue { background: linear-gradient(160deg, #ffffff 20%, #1fa7b5 60%, #d7edf0 100%); }
</style>
</head>
<body>
  <div class="page">
    <div class="brand">
      <div class="brand-dot"></div>
      <div class="brand-name">VELTRANO</div>
    </div>

    <header class="masthead">
      <div class="masthead-title">BUSINESS <span>SOLUTIONS</span></div>
      <div class="masthead-tagline">OUR SOLUTIONS MAKES YOUR BUSINESS BETTER!</div>
    </header>

    <nav class="top-nav">
      <a href="#">HOME</a><a href="#">ABOUT</a><a href="#">F.A.Q.</a><a href="#">COTNACT</a>
    </nav>

    <div class="content-panel"></div>

    <nav class="side-nav">
      <a href="#">HOME</a>
      <a href="#">OUR SERVICES</a>
      <a href="#">WHY US!</a>
      <a href="#">REFERENCES</a>
      <a href="#">F.A.Q.</a>
      <a href="#">CONTACT</a>
    </nav>

    <main class="main">
      <h1>WELCOME DEAR FRIEND</h1>
      <p>Lorem ipsum dolor sit amet, consectetur adipiscing elit. Sed sed turpis in quam lacinia pulvinar. Aliquam arcu nisl, aliquam eget tincidunt ut, consequat sed nibh. Nunc aliquet ligula in libero lacinia consectetur. Nam semper mi eu dui porta quis hendrerit risus rutrum. In in urna orci, non scelerisque risus.</p>
      <p>Curabitur nec nunc nec arcu venenatis malesuada a in quam. Vivamus dignissim tempor neque, non semper eros dictum ac. Donec tristique tristique massa in auctor. Vestibulum vel ipsum commodo leo molestie fermentum non nec ligula. Mauris in gravida nisl. Phasellus nisl orci, vulputate ut placerat vel, sagittis sed enim.</p>
      <p>Quisque tempus nibh nec quam bibendum venenatis. Cras fermentum lobortis bibendum. Cras id mattis nibh. Sed eget neque eros, in ultrices metus. Sed interdum lobortis erat, ultrices sagittis odio accumsan ut. Donec luctus risus sed turpis gravida nec mattis risus venenatis. Suspendisse quis augue et nulla eleifend viverra. Aenean risus sem, pretium in pulvinar vitae, molestie at leo.</p>
      <div class="chart-row">
        <div class="chart chart-warm" role="img" aria-label="3D bar chart illustration in red and amber with a rising arrow"></div>
        <div class="chart chart-green" role="img" aria-label="3D bar chart illustration in lime and green with a rising arrow"></div>
        <div class="chart chart-blue" role="img" aria-label="3D bar chart illustration in teal and blue with a rising arrow"></div>
      </div>
      <p>In in urna orci, non scelerisque risus. Curabitur nec nunc nec arcu venenatis malesuada a in quam. Vivamus dignissim tempor neque, non semper eros dictum ac. Donec tristique tristique massa in auctor. Vestibulum vel ipsum commodo leo molestie fermentum non nec ligula. Mauris in gravida nisl. Phasellus nisl orci, vulputate ut placerat vel, sagittis sed enim. Quisque tempus nibh nec quam bibendum venenatis.</p>
      <p>Cras fermentum lobortis bibendum. Cras id mattis nibh. Sed eget neque eros, in ultrices metus. Sed interdum lobortis erat, ultrices sagittis odio accumsan ut.</p>
    </main>
  </div>
</body>
</html>
```